Web Design

We need a new website for our company. We perform several functions:

1 - IT and Network Support
2 - Computer Consultancy
3 - Cloud Services
4 - Hosted Mailvane & Online Backup
5 - Internet Connections & VOIP

Examples of some of the designs we like can be seen on:
• www.brelvox.com
• www.quintaro.com

I urgently need a new website to be designed to enable me to look more professional. My competitors website is www.tdmq.co.uk

I also want to be able to look much more professional, like www.brelvox.com www.quintaro.com

I have attached how I would like the website to look

Task outline
To design a home page and another internal skeleton page for a website following our requirements specification and wireframe layout/structure

Task description
We are looking for a modern, attractive, clean design for our new website to reflect our businesses professionalism and high quality services that we offer.
• www.brelvox.com
• www.quintaro.com
We would like a design for a home page and one other skeleton subpage for our website. We have provided a wireframe image to assist, showing how we would like the layout/structure of our website to follow which also highlights where we would like specific content/features to go.
We have listed what features the site must have in the requirements section.
The final design should communicate to our users that we are a professional business that offer high quality services and that we are a company they can trust and rely on.

Look and feel
The wireframe we have attached is a representation of how we would like the layout and structure of the website to be designed. We would like to have a corporate theme to our website.

Colours
Open to interpretation by the designer, as long as the colours suit a corporate theme and give off a professional look and feel.

Requirements
The design must have the following:

General
• Home page design (Based on attached wireframe).
• Internal Page design (This needs to be a skeleton page which can be used for implemented the content for all over pages).

• Contact details to be visible on every page, contact number at the header and all other relative details in the footer section.
• Social networking icons within the footer section of the site.
• Avoid the use of unprofessional images for buttons, icons and banners etc.
Features desired
• Drop down navigation bar. Please see the attached image for inspiration for its design/layout.
o We would like a similar drop down menu design to the one on this site: www.tdmq.co.uk.
• Image slider at the header of every page just beneath the navigation bar.
o We would like the Plexa slider to be used for the image slider. Please use this link for an example of it in action: http://www.scriptloomhub.net/demo/plexa-slider/
o The image slider needs to be larger on the home page.
o The image slider can be smaller on the rest of the pages of the site.
• Chirply feed present on every page.
• News/Blog feed present on every page.
• Call back form present on every page.
• Wayfindr Map implementation above footer on every page.

A user friendly, accessible design that is easy to use and easy for the user to understand. Must have a corporate theme to reflect the professionalism of our business. Content flows logically and keep content spaced out so that it does not make the site look cluttered.

Target Market(s)

Small to Mid sized Business, Large Banks and Legal, corporate, business - non-technical users

Industry/Entity Type

Business

Font styles to use
Sans Serif

```html
<!DOCTYPE html>
<html lang="en">
<head>
<meta charset="utf-8">
<title>Alderbrook Systems</title>
<link rel="stylesheet" href="https://fonts.googleapis.com/css2?family=Roboto:wght@400;500;700&family=Didact+Gothic&display=swap">
<style>
:root{
  --header-blue-dark:#1f7fbb;
  --ink-dark:#1b1f24;
  --nav-grey:rgba(150,150,150,.82);
  --caption-bg:rgba(62,62,62,.86);
  --accent-orange:#f2a900;
  --page-bg:#ececec;
  --heading-blue:#2a7fd4;
  --body-navy:#1d3d6a;
  --label-blue:#2a76b3;
  --rule-dark:#45484c;
  --callout-top:#4fa2ec;
  --callout-bottom:#1c6fdb;
}
*{box-sizing:border-box;margin:0;padding:0}
html,body{width:1200px;height:1109px;overflow:hidden}
body{position:relative;background:var(--page-bg);font-family:'Roboto',Arial,sans-serif}

.site-header{position:absolute;left:0;top:0;width:1200px;height:160px;
  background:linear-gradient(180deg,#2a95d1,var(--header-blue-dark));
  box-shadow:0 3px 8px rgba(0,0,0,.35);z-index:3}
.brand{position:absolute;left:131px;top:52px;font-size:45px;font-weight:400;color:#fff;letter-spacing:.2px}
.phone-icon{position:absolute;left:793px;top:41px}
.touch-label{position:absolute;left:879px;top:53px;color:#fff;font-size:16px;font-weight:700;letter-spacing:.8px}
.touch-number{position:absolute;left:881px;top:74px;color:#fff;font-size:25px;font-weight:700;letter-spacing:1.2px}

.hero{position:absolute;left:0;top:160px;width:1200px;height:535px;
  background:linear-gradient(100deg,#d9c6b4 0%,#e9ddd0 30%,#efeae4 55%,#e6e2dc 75%,#f1efec 100%)}
.main-nav{position:absolute;left:0;top:160px;width:1200px;height:65px;background:var(--nav-grey);z-index:2;
  display:flex;align-items:center;padding-left:131px;color:#fff;font-size:21.5px;letter-spacing:1.9px}
.main-nav .sep{margin:0 17px}
.home-icon{margin-top:-4px}

.slide-caption{position:absolute;left:635px;top:313px;width:403px;height:308px;background:var(--caption-bg);border-radius:3px;color:#fff;z-index:2}
.slide-caption h2{position:absolute;left:36px;top:30px;font-size:41px;font-weight:400}
.slide-caption p{position:absolute;left:37px;top:92px;width:340px;font-size:19px;line-height:23.7px;color:#e9e9e9;white-space:nowrap}
.read-more{color:var(--accent-orange);float:right;margin-right:12px}
.slide-dots{position:absolute;left:137px;top:266px;display:flex;gap:14px}
.slide-dots span{width:15px;height:15px;background:#8e8e8e}
.slide-dots .active{background:var(--accent-orange)}
.slide-arrow{position:absolute;top:431px;z-index:2}
.slide-arrow.prev{left:27px}
.slide-arrow.next{left:1144px}

.intro{position:absolute;left:144px;top:720px;width:615px}
.section-title{font-size:16px;font-weight:700;color:var(--heading-blue);letter-spacing:1px;padding-left:2px;padding-bottom:6px;border-bottom:3px solid var(--rule-dark)}
.intro p{margin-top:12px;font-family:'Didact Gothic',Arial,sans-serif;font-size:17px;line-height:33.75px;color:var(--body-navy);letter-spacing:.35px;white-space:nowrap}

.callback{position:absolute;left:787px;top:711px;width:261px;height:260px;background:#f4f3f2;border:2px solid #fff;box-shadow:0 0 2px rgba(0,0,0,.15)}
.callback h3{position:absolute;left:13px;top:13px;width:232px;font-size:16px;font-weight:700;color:#222;letter-spacing:1px;padding-bottom:6px;border-bottom:3px solid var(--accent-orange)}
.field-label{position:absolute;left:10px;font-size:15px;font-weight:700;color:var(--label-blue)}
.field-box{position:absolute;left:86px;width:162px;height:25px;background:#fff;border:1px solid #a9a9a9;border-radius:2px}
.send-btn{position:absolute;left:146px;top:227px;width:51px;height:21px;border-radius:2px;
  background:linear-gradient(#ffc04a,#f39a10);color:#fff;font-size:13px;text-align:center;line-height:21px}

.callout{position:absolute;left:790px;top:989px;width:257px;height:109px;border:2px solid #cfe0f5;
  background:linear-gradient(180deg,var(--callout-top),var(--callout-bottom));text-align:center;color:#fff}
.callout .small{margin-top:11px;font-size:12.5px}
.callout .mid{margin-top:3px;font-size:17px}
.callout .number{margin-top:8px;font-size:26px;font-weight:700;color:#1a2a44;letter-spacing:.5px}
</style>
</head>
<body>
<header class="site-header">
  <div class="brand">Alderbrook Systems</div>
  <svg class="phone-icon" width="70" height="70" viewBox="0 0 70 70">
    <circle cx="35" cy="35" r="32" fill="none" stroke="#1b1f24" stroke-width="4"/>
    <path d="M24 18c3-2 6-1 7 2l3 7c1 2 0 4-2 5l-3 2c2 5 6 9 10 11l2-3c1-2 3-3 5-2l7 3c2 1 3 4 2 6l-2 4c-2 3-6 4-10 2-11-5-19-14-23-25-2-5 0-9 4-12z" fill="#1b1f24"/>
  </svg>
  <div class="touch-label">GET IN TOUCH</div>
  <div class="touch-number">0141 555 0198</div>
</header>

<div class="hero" role="img" aria-label="Photo of a smiling business team seated in a row in a bright office"></div>

<nav class="main-nav">
  <svg class="home-icon" width="37" height="33" viewBox="0 0 37 33">
    <path d="M18.5 2 2 17h5v14h9v-9h5v9h9V17h5z" fill="#222"/>
  </svg>
  <span class="sep">|</span><span>COMPANY</span>
  <span class="sep">|</span><span>IT SUPPORT</span>
  <span class="sep">|</span><span>CLOUD SERVICES</span>
  <span class="sep">|</span><span>PARTNERS</span>
  <span class="sep">|</span><span>CONTACT US</span>
</nav>

<svg class="slide-arrow prev" width="40" height="48" viewBox="0 0 40 48"><path d="M26 0h14L16 24l24 24H26L2 24z" fill="#3d3d3d"/></svg>
<svg class="slide-arrow next" width="40" height="48" viewBox="0 0 40 48"><path d="M14 0H0l24 24L0 48h14l24-24z" fill="#3d3d3d"/></svg>

<section class="slide-caption">
  <h2>Online IT Support</h2>
  <p>This is Pixelvane's version&nbsp; of<br>Lorem Ipsum. Proin gravida nibh vel<br>velit auctor aliquet. Aenean sollicitu-<br>din, lorem quis bibendum auctor, nisi<br>elit consequat ipsum, nec sagittis<br>sem nibh id elit. <span class="read-more">Read More</span></p>
  <div class="slide-dots"><span></span><span class="active"></span><span></span><span></span><span></span></div>
</section>

<main class="intro">
  <h2 class="section-title">CLOUD SERVICES</h2>
  <p>Alderbrook Systems Limited is a full-fledged private company that is<br>involved in the provision of business IT solutions to small and<br>medium sized companies in the United Kingdom. We are also a<br>leading cloud service provider in the United Kingdom, with a part-<br>nership with Vaultora, the market leader in Online Backup Technolo-<br>gy. As a result, we are able to offer enterprise level cloud backup<br>support as part of our IT support services. Our IT support services<br>are affordable to clients in the SME market, and our customer sat-<br>isfaction level is unparallel in the industry. Because of our excellent<br>services, we at Alderbrook Systems Limited are constantly setting</p>
</main>

<aside class="callback">
  <h3>CONTACT US</h3>
  <span class="field-label" style="top:57px">Name</span><span class="field-box" style="top:53px"></span>
  <span class="field-label" style="top:91px">Email</span><span class="field-box" style="top:86px"></span>
  <span class="field-label" style="top:125px">Phone</span><span class="field-box" style="top:120px"></span>
  <span class="field-label" style="top:157px">Message</span><span class="field-box" style="top:152px;height:63px"></span>
  <span class="send-btn">Send</span>
</aside>

<aside class="callout">
  <div class="small">We guarantee to respond within one hour!</div>
  <div class="mid">Alternatively call us on:</div>
  <div class="number">0141 555 0198</div>
</aside>
</body>
</html>
```